Thank You Card

I'm looking for a thank you card design using our logo and other graphics. We are an essential business and our employees (Electricians) have done an incredible job staying healthy and safe during the COVID-19 pandemic, I want to send each a thank you card.

```html
<!DOCTYPE html>
<html lang="en">
<head>
<meta charset="utf-8">
<title>Thank You Card</title>
<link rel="stylesheet" href="https://fonts.googleapis.com/css2?family=Alegreya+Sans:wght@400;700&family=Satisfy&display=swap">
<style>
  :root {
    --paper-light: #f6efee;
    --paper-mid: #ece6ea;
    --paper-cool: #dfe3ec;
    --bulb-amber: #f5a623;
    --bulb-peach: #f7c9b0;
    --bulb-cyan: #3fb5e0;
    --bulb-blue: #5f8fe6;
    --bulb-pink: #e9a9d6;
    --disc-deep: rgba(80, 88, 165, 0.88);
    --disc-soft: rgba(96, 106, 178, 0.38);
    --band-lilac: rgba(180, 160, 232, 0.82);
    --band-violet: rgba(160, 120, 218, 0.85);
    --band-sky: rgba(170, 205, 235, 0.55);
    --frame: rgba(255, 255, 255, 0.72);
    --ink-white: #ffffff;
    --brand-blue: #1f38a6;
  }
  * { margin: 0; padding: 0; box-sizing: border-box; }
  html, body { width: 1200px; height: 857px; overflow: hidden; background: #ffffff; }
  .card {
    position: relative;
    width: 1200px;
    height: 857px;
    overflow: hidden;
    background:
      radial-gradient(ellipse at 30% 40%, var(--paper-light) 0%, var(--paper-mid) 55%, var(--paper-cool) 100%);
  }
  .card-art { position: absolute; inset: 0; width: 1200px; height: 857px; }
  .card-art svg { display: block; }
  .greeting-list {
    position: absolute;
    left: 740px;
    top: 92px;
    width: 434px;
    list-style: none;
    text-align: center;
    font-family: "Alegreya Sans", sans-serif;
    font-weight: 400;
    font-size: 36px;
    line-height: 1;
    color: var(--ink-white);
  }
  .greeting-list li { height: 91px; }
  .thank-you {
    position: absolute;
    left: 0;
    top: 560px;
    width: 1200px;
    text-align: center;
    padding-left: 10px;
    font-family: "Satisfy", cursive;
    font-size: 150px;
    line-height: 1.2;
    color: var(--ink-white);
  }
  .brand-name {
    position: absolute;
    left: 66px;
    top: 318px;
    height: 222px;
    writing-mode: vertical-rl;
    font-family: "Alegreya Sans", sans-serif;
    font-weight: 700;
    font-size: 30px;
    line-height: 36px;
    letter-spacing: 1px;
    color: var(--brand-blue);
    text-align: center;
  }
</style>
</head>
<body>
<main class="card">
  <div class="card-art">
    <svg width="1200" height="857" viewBox="0 0 1200 857" xmlns="http://www.w3.org/2000/svg">
      <defs>
        <linearGradient id="bulb-warm" x1="0" y1="0" x2="0" y2="1">
          <stop offset="0" stop-color="var(--bulb-amber)"/>
          <stop offset="0.5" stop-color="var(--bulb-peach)"/>
          <stop offset="0.78" stop-color="#cfe6ef"/>
          <stop offset="1" stop-color="var(--bulb-cyan)"/>
        </linearGradient>
        <radialGradient id="bulb-cool" cx="0.5" cy="0.45" r="0.6">
          <stop offset="0" stop-color="var(--bulb-pink)"/>
          <stop offset="0.6" stop-color="var(--bulb-blue)"/>
          <stop offset="1" stop-color="#4aa6e8"/>
        </radialGradient>
        <linearGradient id="band-fill" x1="0" y1="0" x2="1" y2="0">
          <stop offset="0" stop-color="var(--band-lilac)"/>
          <stop offset="0.5" stop-color="rgba(170,160,235,0.75)"/>
          <stop offset="1" stop-color="var(--band-violet)"/>
        </linearGradient>
      </defs>

      <circle class="bulb bulb-top" role="img" aria-label="Photograph of a glowing vintage filament light bulb" cx="366" cy="106" r="240" fill="url(#bulb-warm)"/>

      <circle class="disc disc-soft" cx="1086" cy="114" r="440" fill="var(--disc-soft)"/>
      <circle class="disc disc-deep" cx="1046" cy="143" r="343" fill="var(--disc-deep)"/>

      <circle class="bulb bulb-bottom" role="img" aria-label="Photograph of a clear filament light bulb in cool blue light" cx="639" cy="737" r="197" fill="url(#bulb-cool)"/>

      <rect class="band band-main" x="0" y="553" width="1200" height="237" fill="url(#band-fill)"/>
      <rect class="band band-foot" x="0" y="790" width="1200" height="42" fill="var(--band-sky)"/>

      <rect class="frame" x="23" y="19" width="1154" height="819" fill="none" stroke="var(--frame)" stroke-width="12"/>
    </svg>
  </div>

  <div class="brand-name">BRIGHTLINE<br>SERVICE CO</div>

  <ul class="greeting-list">
    <li>For doing incredible job</li>
    <li>For staying healthy</li>
    <li>For staying safe</li>
  </ul>

  <p class="thank-you">Thank you</p>
</main>
</body>
</html>
```